Oil and Gas Letterhead Design Tweak

Simple letterhead information and design tweak.

Please note, we don't want to change the design or logo of the letterhead only the small changes mentioned below.

We need to change the company name up top to "Northvale Petrotek FZCO"

Also, we need to include in the footer the following information. I have attached an image of roughly how we would like to have it displayed in the footer.

Footer Details:

Northvale Petrotek FZCO,
Unit No. 2378, FZCO Trade Hub, level No. 1, K&P 7, Dubai, United Arab Emirates
Northvale Petrotek FZCO is registered as a free zone company under the rules & regulations of FZCO

Target Market(s)

O&G Market

Industry/Entity Type

Oil And Gas

Font styles to use
Sans Serif

Colors

Designer to choose colors to be used in the design.

Requirements
Must have
• Change the company name to Northvale Petrotek FZCO
• Include the footer on the bottom of the first and continuation page
Should not have
• Should not change the design or logo of the letterhead, only the specified changes mentioned above

```html
<!DOCTYPE html>
<html lang="en">
<head>
<meta charset="utf-8">
<title>Northvale Petrotek FZCO – Letterhead</title>
<link rel="stylesheet" href="https://fonts.googleapis.com/css2?family=Open+Sans:wght@400;600;700&family=EB+Garamond:wght@400&display=swap">
<style>
  :root {
    --backdrop: #c4c8cb;
    --paper: #ffffff;
    --brand-blue: #0f4fa3;
    --brand-red: #e31e26;
    --ink: #2a2a2a;
  }
  * { margin: 0; padding: 0; box-sizing: border-box; }
  html, body { width: 1200px; height: 900px; overflow: hidden; }
  body {
    background: var(--backdrop);
    font-family: "Open Sans", Arial, sans-serif;
    position: relative;
  }
  .sheet {
    position: absolute;
    top: 164px;
    width: 404px;
    height: 570px;
    background: var(--paper);
    overflow: hidden;
  }
  .sheet--first { left: 173px; }
  .sheet--continuation { left: 620px; }
  .sheet svg.trim { position: absolute; left: 0; top: 0; }

  .brand-lockup {
    position: absolute;
    left: 100px;
    top: 20px;
    display: flex;
    align-items: center;
    gap: 8px;
  }
  .brand-lockup__dot {
    width: 14px; height: 14px; border-radius: 50%;
    background: var(--brand-blue);
  }
  .brand-lockup__name {
    font-size: 12px;
    font-weight: 400;
    letter-spacing: 0.06em;
    color: var(--ink);
  }

  .company-name {
    position: absolute;
    font-size: 12.5px;
    font-weight: 700;
    color: var(--brand-blue);
    white-space: nowrap;
  }
  .sheet--first .company-name {
    left: 18px; top: 52px;
    padding-bottom: 2px;
    border-bottom: 1px solid var(--brand-red);
  }
  .sheet--continuation .company-name { left: 16px; top: 30px; }

  .footer {
    position: absolute;
    left: 18px;
    font-size: 6px;
    line-height: 8px;
    color: var(--ink);
    white-space: nowrap;
  }
  .footer__name { color: var(--brand-red); margin-bottom: 6px; font-family: "Open Sans", Arial, sans-serif; }
  .sheet--first .footer { top: 518px; font-family: "EB Garamond", Georgia, serif; }
  .sheet--continuation .footer { left: 16px; top: 526px; font-size: 6.2px; line-height: 7.8px; }
  .sheet--continuation .footer__name { margin-bottom: 2px; }
  .footer__name strong { font-weight: 700; }

  .footer-mark {
    position: absolute;
    left: 307px;
    top: 524px;
    width: 50px;
    display: flex;
    flex-direction: column;
    align-items: center;
    gap: 4px;
  }
  .footer-mark__dot {
    width: 12px; height: 12px; border-radius: 50%;
    background: var(--brand-blue);
  }
  .footer-mark__name {
    font-size: 5px;
    line-height: 5.5px;
    text-align: center;
    letter-spacing: 0.04em;
    color: var(--ink);
  }
</style>
</head>
<body>

  <section class="sheet sheet--first" aria-label="First page letterhead">
    <svg class="trim" width="404" height="570" viewBox="0 0 404 570" aria-hidden="true">
      <polygon points="0,0 92,0 89,7 0,7" fill="var(--brand-blue)"/>
      <polygon points="125,0 404,0 404,7 129,7" fill="var(--brand-red)"/>
      <polygon points="294,563 313,563 309,570 290,570" fill="var(--brand-blue)"/>
      <polygon points="316,563 331,563 335,570 312,570" fill="var(--brand-red)"/>
    </svg>

    <div class="brand-lockup">
      <span class="brand-lockup__dot"></span>
      <span class="brand-lockup__name">NORTHVALE ENERGY GROUP</span>
    </div>

    <h1 class="company-name">Northvale Petrotek FZCO</h1>

    <footer class="footer">
      <p class="footer__name">Northvale Petrotek FZCO,</p>
      <p>Unit No. 2378, FZCO Trade Hub,</p>
      <p>level No. 1, K&amp;P 7, Dubai, United Arab Emirates</p>
      <p>Northvale Petrotek FZCO is registered as a free zone company under the rules &amp; regulations of FZCO</p>
    </footer>
  </section>

  <section class="sheet sheet--continuation" aria-label="Continuation page letterhead">
    <svg class="trim" width="404" height="570" viewBox="0 0 404 570" aria-hidden="true">
      <polygon points="297,0 332,0 326,12 303,12" fill="var(--brand-blue)"/>
      <polygon points="336,0 361,0 355,12 330,12" fill="var(--brand-red)"/>
      <polygon points="0,562 302,562 298,570 0,570" fill="var(--brand-blue)"/>
      <polygon points="355,558 404,558 404,570 363,570" fill="var(--brand-red)"/>
    </svg>

    <h1 class="company-name">Northvale Petrotek FZCO</h1>

    <footer class="footer">
      <p class="footer__name">Northvale Petrotek <strong>FZCO,</strong></p>
      <p>Unit No. 2378, FZCO Trade Hub,</p>
      <p>level No. 1, K&amp;P 7, Dubai, United Arab Emirates</p>
      <p>Northvale Petrotek FZCO is registered as a free zone company under the rules &amp; regulations of FZCO</p>
    </footer>

    <div class="footer-mark">
      <span class="footer-mark__dot"></span>
      <span class="footer-mark__name">NORTHVALE<br>ENERGY GROUP</span>
    </div>
  </section>

</body>
</html>
```